Surgical Procedure Room Letterhead

PLEASE DO NOT MAKE YOUR LETTERHEAD SIMILAR TO THE ONE I AM INCLUDING IN MY UPLOADS

Hello! I need my logo used to make a very clean, professional, simple letterhead that has all the pertinent information in it:
Location: 4182 NW 38th Lane, Suite 500
Tamarac, FL 33967
Phone: 954-218-4650
Fax: 800-642-9082

Can you please put this all on a word document that is easily editable? I will include my practice letterhead as an example ONLY of how easy it should be to write below the letterhead. Please don't make this letterhead the same as the one I am including in this example. They are two separate businesses.

Target Market(s)

Insurance companies

Industry/Entity Type

medical

Requirements
Must have
• classiness, elegance, simplicity
Should not have
• Please don't make your letterhead the same as the one that I included in my uploads

```html
<!DOCTYPE html>
<html lang="en">
<head>
<meta charset="utf-8">
<title>Vantage Suites Letterhead</title>
<link rel="stylesheet" href="https://fonts.googleapis.com/css2?family=Montserrat:wght@400;600&display=swap">
<style>
  :root {
    --navy: #1a3158;
    --gold: #d9b13f;
    --backdrop: #dcdcdc;
    --paper: #ffffff;
    --ink: #2b2f38;
  }
  * { margin: 0; padding: 0; box-sizing: border-box; }
  html, body {
    width: 1153px;
    height: 1200px;
    overflow: hidden;
    background: var(--backdrop);
  }
  .letterhead {
    position: absolute;
    left: 124px;
    top: 15px;
    width: 904px;
    height: 1170px;
    background: var(--paper);
    font-family: "Montserrat", sans-serif;
  }
  .brand {
    position: absolute;
    left: 56px;
    top: 52px;
    display: flex;
    align-items: center;
    gap: 18px;
  }
  .brand-mark {
    width: 76px;
    height: 76px;
    border-radius: 50%;
    background: var(--gold);
    flex: none;
  }
  .brand-name {
    font-weight: 600;
    font-size: 33px;
    line-height: 36px;
    letter-spacing: 1.5px;
    text-transform: uppercase;
    color: var(--navy);
  }
  .contact-divider {
    position: absolute;
    left: 551px;
    top: 51px;
    width: 2px;
    height: 80px;
    background: var(--navy);
  }
  .contact {
    position: absolute;
    left: 566px;
    top: 46px;
    list-style: none;
    font-size: 17px;
    line-height: 22px;
    color: var(--ink);
  }
  .contact li {
    display: flex;
    align-items: center;
    padding-left: 21px;
    position: relative;
  }
  .contact-icon {
    position: absolute;
    left: 0;
    top: 4px;
    width: 15px;
    height: 15px;
    fill: var(--navy);
  }
  .header-rule {
    position: absolute;
    left: 57px;
    top: 157px;
    width: 791px;
    height: 2px;
    background: var(--navy);
  }
  .footer-band {
    position: absolute;
    left: 0;
    bottom: 0;
    width: 904px;
    height: 39px;
    display: block;
  }
</style>
</head>
<body>
  <main class="letterhead">
    <header>
      <div class="brand">
        <span class="brand-mark"></span>
        <span class="brand-name">Vantage<br>Suites</span>
      </div>

      <span class="contact-divider"></span>

      <ul class="contact">
        <li>
          <svg class="contact-icon" viewBox="0 0 16 16" aria-hidden="true">
            <path d="M8 0.5a5.5 5.5 0 0 0-5.5 5.5c0 4 5.5 9.5 5.5 9.5s5.5-5.5 5.5-9.5A5.5 5.5 0 0 0 8 0.5zm0 7.8a2.3 2.3 0 1 1 0-4.6 2.3 2.3 0 0 1 0 4.6z"/>
          </svg>
          4182 NW 38th Lane, Suite 500
        </li>
        <li>Tamarac, FL 33967</li>
        <li>
          <svg class="contact-icon" viewBox="0 0 16 16" aria-hidden="true">
            <path d="M1 6c0-2 3-3.5 7-3.5S15 4 15 6v1.5h-3.5V6h-7v1.5H1zM3.5 8.5h9l1.5 5H2z"/>
          </svg>
          954-218-4650
        </li>
        <li>
          <svg class="contact-icon" viewBox="0 0 16 16" aria-hidden="true">
            <path d="M4 1h8v4H4zM1 6h14v6h-3v-2H4v2H1zM5 11h6v4H5z"/>
          </svg>
          800-642-9082
        </li>
      </ul>

      <span class="header-rule"></span>
    </header>

    <svg class="footer-band" viewBox="0 0 904 39" aria-hidden="true">
      <polygon points="0,0 501,0 441,39 0,39" fill="var(--navy)"/>
      <polygon points="517,0 904,0 904,39 455,39" fill="var(--gold)"/>
    </svg>
  </main>
</body>
</html>
```